A unique communication angle to crowdfunding

Looking for a fresh redesign of a crowd funding website that deals in real estate. I already have the content, but am looking to take the design to the next level.

Existing real estate crowd funding sites focus on the real estate. I want to explore communication angle that:
- puts the investor in the centre of the communication: "become a baron"
- highlights the international nature (international properties, international investors)

There's also quite a lot of copy on the site, as we need to explain the service in quite a bit of detail. There's room to reduce the copy and replace with graphics. Could also consider clicking to see different text (see our difference section in http://galatownfeed.com)

The backend of the platform is already being worked on by a specialist crowd funding service provider.

In total there are 5 pages to be designed.

The homepage is really important. Right now it looks quite dated. It doesn't have a great layout. Note there is no mobile version of the website, so the pages need to be seen well on mobile devices. When looking at the brief, refer to the following links too:

current website:
http://pooltenant.com

some revisions made so far:
http://preview.fundmerrow.com/2G5GO2

Attached are logo files and another file which contained copy for the pages. No need to rework the logo.

Please make sure to use the same copy in the brief on the webpages, to ensure the layouts work. Designers are free to propose images they feel work on the pages.

I would like to see if rather than tweaking the pages, it's possible to come up with a better design concept. If the 5 pages are accepted, there's a chance I'll request an additional 4 pages.
Updates

Please note the font used in the logo is called "harabara" in case you decide to use it in any of the titles, etc.

Please note there is one additional page for which we would like to review designs. Note the page would be a template to be used on all future real estate detail pages. Here is an example of the current design for reference:

http://pooltenant.com/projects/view/14

In total there are 5 page designs required, (homepage + 4)

Thank you

FYI -

Just a quick note to give information from similar UK real estate crowdfunding sites:
http://www.estatewren.co.uk
http://plotharbor.co.uk
https://www.tilgarcap.com

Of the above, only plotharbor has a nice clean looking landing page. Information is clear and well laid out.

Hi all, just uploaded a new file in the brief. Contains some comments and a website reference. I thought it may help to explain how we could convey international aspect as well as how we could convey images in a more modern way. This is an option you can consider, but its entirely up to you how how answer the brief. Thanks!

We would like to let you know that we have just shortlisted the best designs. Together with that, we have also passed some detailed feedback to all designers who weren't shortlisted. If we didn't contact you, please let us know. If you haven't submitted a design or are working on revisions, please note these will no longer be taken into account now. We hope you understand that we need to close the project today. Thank you all once again for your great work and design concepts. Here's hoping we meet again on a future design brief. Cheers, pooltenant team.

Target Market(s)

At the moment, only rich are able to buy real estate. With this service, anyone can become a landlord. Target buyers:

Young professionals, looking to diversify from stock market and lower risk
People nearing retirement, looking for stable rental incomes
Retirees - looking to supplement pensions with possibility of capital gains
Parents - looking for a way to save long term for their children (instead of low interest paying bank accounts)

Industry/Entity Type

Communication

Font styles to use
Sans Serif
Other font styles liked:
• harabara

Colors
add136
f5f9eb
959595
000000

Requirements
Must have
• Overall, the site must convey "whoever you are, you too can become a landlord", and that you don't need to be wealthy to invest in real estate. See

Communication should put the investor (or the baron) at the centre. The investor can be any of those described in the target market.

Show the aspirational side of property ownership.

In addition to the investor/baron character, the second main theme is international. No other real estate crowdfunding website highlights this.
Nice to have
• Banner could show different consumer types, to illustrate that the service can appeal to many different profiles. Refer to attached file "home page reference - plainasdew.com" as an example of how this could be done.

Aim to show the international side of the service. Properties around the world, investors around the world.

```html
<!DOCTYPE html>
<html lang="en">
<head>
<meta charset="utf-8">
<title>pooltenant — Become a Baron</title>
<link href="https://fonts.googleapis.com/css2?family=Montserrat:wght@400;700&family=Open+Sans:wght@300;400;600;700&display=swap" rel="stylesheet">
<style>
:root{
  --green:#add136;
  --green-dark:#8fb222;
  --green-soft:#f5f9eb;
  --blue:#2aa3d1;
  --blue-soft:#e4f4f9;
  --grey:#959595;
  --grey-light:#e6e6e6;
  --ink:#222222;
  --black:#000000;
  --white:#ffffff;
}
*{box-sizing:border-box;margin:0;padding:0}
html,body{width:1200px;height:3693px;overflow:hidden}
body{font-family:"Open Sans",Arial,sans-serif;color:var(--ink);background:var(--white);position:relative}
section,header,footer{position:absolute;left:0;width:1200px}
.abs{position:absolute}
.brand{display:flex;align-items:center;gap:10px;font-weight:700;font-size:26px;color:var(--green);white-space:nowrap}
.brand-dot{width:26px;height:26px;border-radius:50%;background:var(--green)}
.btn{display:inline-flex;align-items:center;justify-content:center;font-weight:600;color:var(--white);background:var(--green);border-radius:4px;text-decoration:none;white-space:nowrap}

/* header */
.site-header{top:0;height:83px;border-bottom:1px solid var(--grey-light)}
.site-header .brand{left:133px;top:26px}
.main-nav{left:425px;top:33px;display:flex;gap:34px;font-size:12px;text-transform:uppercase;color:var(--grey);font-weight:600;white-space:nowrap}
.login{left:978px;top:26px;width:92px;height:31px;border-radius:16px;font-size:12px}

/* hero */
.hero{top:83px;height:525px;overflow:hidden}
.hero-photo{position:absolute;inset:0;background:linear-gradient(120deg,#cfd9dc 0%,#a9b8b8 25%,#b48763 50%,#8a6246 75%,#5f4a3a 100%)}
.hero-shade{position:absolute;inset:0;background:linear-gradient(180deg,rgba(0,0,0,.1),rgba(0,0,0,.25))}
.hero h1{position:absolute;left:0;width:1200px;top:140px;text-align:center;font-weight:400;font-size:40px;color:var(--white)}
.hero .sub{position:absolute;left:0;width:1200px;top:212px;text-align:center;font-size:25px;color:var(--white);padding-left:160px}
.hero .btn{left:489px;top:299px;width:232px;height:66px;font-size:18px}
.slider-arrows{left:1010px;top:455px;display:flex;gap:22px}

/* intro */
.intro{top:608px;height:516px;text-align:center}
.intro-mark{left:575px;top:60px;width:50px;height:50px;border-radius:50%;background:var(--green)}
.intro h2{position:absolute;top:165px;width:1200px;font-family:"Montserrat",Arial,sans-serif;font-weight:400;font-size:25px;letter-spacing:2px;line-height:53px;color:var(--ink)}
.intro p{position:absolute;left:220px;width:760px;font-size:16px;line-height:27px;color:var(--grey)}

/* features tabs */
.features{top:1124px;height:455px}
.tab{display:flex;align-items:center;gap:22px;font-size:27px;font-weight:300;color:#555;white-space:nowrap}
.tab-num{width:40px;height:40px;border-radius:50%;background:#333;color:var(--white);font-size:17px;font-weight:600;display:flex;align-items:center;justify-content:center}
.tab.active .tab-num{background:var(--white);border:2px solid var(--green);color:var(--green)}
.tab-line{left:146px;top:161px;width:904px;height:2px;background:var(--grey-light)}
.tab-line span{display:block;width:200px;height:3px;background:var(--green)}
.feature-art{left:226px;top:239px;width:106px;height:100px;border-radius:8px;background:linear-gradient(180deg,#d6eef7,#7cc6e3)}
.feature-title{left:425px;top:222px;font-size:20px;font-weight:600;color:var(--green);white-space:nowrap}
.feature-text{left:425px;top:262px;width:620px;font-size:14px;line-height:22px;color:var(--grey)}

/* paths */
.paths{top:1579px;height:276px;display:flex}
.path{position:relative;width:600px;height:276px}
.path.buy{background:var(--blue-soft)}
.path.sell{background:var(--green-soft)}
.path-art{position:absolute;border-radius:8px}
.path h3{position:absolute;font-size:20px;font-weight:600;color:var(--ink)}
.path p{position:absolute;width:250px;font-size:14px;line-height:22px;color:#555}
.path .btn{position:absolute;height:48px;width:170px;font-size:13px}

/* projects */
.projects{top:1855px;height:805px}
.projects h2{left:146px;top:68px;font-size:27px;font-weight:600}
.projects .lead{left:146px;top:122px;width:640px;font-size:14px;line-height:22px;color:var(--grey)}
.btn-outline{left:881px;top:100px;width:169px;height:49px;border:1px solid #cfcfcf;border-radius:4px;font-size:13px;color:#444;display:flex;align-items:center;justify-content:center;background:var(--white)}
.card{top:229px;width:273px;height:485px;background:var(--white);border-radius:6px;box-shadow:0 2px 8px rgba(0,0,0,.15);overflow:hidden}
.card-photo{position:relative;height:210px}
.card-new{position:absolute;left:0;top:0}
.card-price{position:absolute;right:0;bottom:0;background:var(--green);color:var(--white);font-size:14px;padding:9px 14px;font-weight:600}
.card-body{padding:20px 22px}
.card h3{font-size:14px;font-weight:700}
.card p{margin-top:10px;font-size:12px;line-height:18px;color:var(--grey)}
.progress{margin-top:22px;height:10px;background:var(--grey-light);border-radius:5px;overflow:hidden}
.progress span{display:block;height:100%;background:var(--green)}
.stats{margin-top:12px;display:flex;justify-content:space-between;font-size:11px;color:#666}
.card-link{margin-top:26px;border-top:1px solid var(--grey-light);padding-top:18px;text-align:center;font-size:13px;color:#444;font-weight:600}
.card-link svg{vertical-align:-2px;margin-left:6px}

/* community */
.community{top:2660px;height:664px;overflow:hidden}
.community h2{position:absolute;top:40px;width:1200px;text-align:center;font-size:34px;font-weight:600;color:var(--green)}
.community .lead{left:300px;top:118px;width:600px;text-align:center;font-size:16px;line-height:27px;color:var(--grey)}
.skyline{left:0;top:200px;width:1200px;height:464px;background:linear-gradient(180deg,#ffffff 0%,#e2e2e2 35%,#b9b9b9 75%,#8e8e8e 100%)}
.quote{top:265px;width:440px;height:150px;background:var(--white);border-radius:6px;box-shadow:0 2px 8px rgba(0,0,0,.12);text-align:center;padding:20px 34px}
.quote h3{font-size:18px;font-weight:600;color:var(--green)}
.quote p{margin-top:12px;font-size:12px;line-height:19px;color:var(--grey)}
.quote-tail{position:absolute;left:46px;bottom:-12px;width:24px;height:24px;background:var(--white);transform:rotate(45deg)}
.author{top:430px;display:flex;align-items:center;gap:16px;font-size:15px;font-weight:600;color:var(--ink);white-space:nowrap}
.avatar{width:60px;height:60px;border-radius:4px;background:#c7b7a5}

/* press */
.press{top:3324px;height:166px}
.press-label{left:123px;top:60px;font-size:12px;font-weight:700;letter-spacing:1px;color:#555}
.press-row{left:123px;top:108px;display:flex;gap:42px;align-items:center}
.press-row span{display:block;height:36px;background:#8a8a8a;border-radius:3px}

/* footer */
.site-footer{top:3490px;height:166px;background:#e9e9e9}
.site-footer .brand{left:123px;top:28px}
.footer-text{left:123px;top:86px;width:440px;font-size:12px;line-height:19px;color:#666}
.footer-nav{top:40px;display:flex;flex-direction:column;gap:12px;font-size:12px;text-transform:uppercase;color:#555;white-space:nowrap}
.group-name{left:930px;top:58px;font-size:26px;font-weight:300;color:#555;line-height:26px}
.bottom-bar{left:0;top:3656px;width:1200px;height:37px;background:#f4f4f4;font-size:11px;color:#777}
.social{left:123px;top:11px;display:flex;gap:10px;align-items:center;white-space:nowrap}
.social i{width:15px;height:15px;background:#555;border-radius:2px;display:block}
.legal{right:123px;top:11px;white-space:nowrap}
</style>
</head>
<body>

<header class="site-header">
  <div class="brand abs"><span class="brand-dot"></span>pooltenant</div>
  <nav class="main-nav abs"><span>Home</span><span>How it works</span><span>Discover a project</span><span>Blog</span><span>Find out more</span></nav>
  <a class="btn login abs">LOGIN</a>
</header>

<section class="hero">
  <div class="hero-photo" role="img" aria-label="Photo of an old brick building with balconies against a pale sky"></div>
  <div class="hero-shade"></div>
  <h1>Property buying is stressful, outdated</h1>
  <p class="sub">&amp; in need of change.</p>
  <a class="btn abs">Become a Member</a>
  <div class="slider-arrows abs">
    <svg width="14" height="22" viewBox="0 0 14 22"><path d="M11 2 3 11l8 9" fill="none" stroke="#fff" stroke-width="3"/></svg>
    <svg width="14" height="22" viewBox="0 0 14 22"><path d="M3 2l8 9-8 9" fill="none" stroke="#fff" stroke-width="3"/></svg>
  </div>
</section>

<section class="intro">
  <div class="intro-mark abs"></div>
  <h2>POOLTENANT IS RECONSTRUCTING A PROPERTY LADDER<br>THAT'S STRONG AND FAIR</h2>
  <p style="top:290px">By harnessing the power of crowds, it's possible to become a landlord in attractive locations around the world without the burden of financing 100% of the purchase.</p>
  <p style="top:357px">Leave the day to day management of your property portfolio to us.<br>Start with as little as 1% in a project and plan your steps to becoming a true baron.</p>
</section>

<section class="features">
  <div class="tab active abs" style="left:146px;top:86px"><span class="tab-num">1</span>Simple</div>
  <div class="tab abs" style="left:440px;top:86px"><span class="tab-num">2</span>Transparent</div>
  <div class="tab abs" style="left:793px;top:86px"><span class="tab-num">3</span>Collaborative</div>
  <div class="tab-line abs"><span></span></div>
  <div class="feature-art abs" role="img" aria-label="Blue line illustration for browsing projects"></div>
  <div class="feature-title abs">Browse projects, like booking a hotel online !</div>
  <p class="feature-text abs">Lorem ipsum dolor sit amet, consectetur adipisicing elit, sed do eiusmod tempor incididunt ut labore et dolore magna aliqua. Ut enim ad minim veniam, quis nostrud exercitation ullamco laboris nisi ut aliquip ex ea commodo consequat.</p>
</section>

<section class="paths">
  <div class="path buy">
    <div class="path-art" role="img" aria-label="Illustration of a floor lamp beside an armchair" style="left:116px;top:49px;width:133px;height:134px;background:linear-gradient(180deg,#cfe9f2,#4bb3d8)"></div>
    <h3 style="left:292px;top:45px">Find Properties</h3>
    <p style="left:292px;top:84px">Sign up to browse the portfolio. Your journey to becoming a real estate baron starts here.</p>
    <a class="btn" style="left:299px;top:183px;background:var(--blue)">Become A Member</a>
  </div>
  <div class="path sell">
    <div class="path-art" role="img" aria-label="Illustration of a wallet with banknotes" style="left:65px;top:55px;width:106px;height:110px;background:linear-gradient(180deg,#b9dd62,#4a4a4a)"></div>
    <h3 style="left:224px;top:45px">Find Buyers</h3>
    <p style="left:224px;top:84px">Sign up to browse the portfolio. Your journey to becoming a real estate baron starts here.</p>
    <a class="btn" style="left:224px;top:183px">Submit Your Project</a>
  </div>
</section>

<section class="projects">
  <h2 class="abs">Featured Projects</h2>
  <p class="lead abs">Brief details of new and popular projects. To view full listings, you will be required to sign up and become a member.</p>
  <div class="btn-outline abs">Become a Member</div>

  <article class="card abs" style="left:146px">
    <div class="card-photo" role="img" aria-label="Photo of a city street lined with tall buildings" style="background:linear-gradient(160deg,#d7dde2,#7f8c97 60%,#4b4f55)">
      <svg class="card-new" width="70" height="70" viewBox="0 0 70 70"><path d="M0 0h70L0 70z" fill="#add136"/><text x="10" y="30" fill="#fff" font-size="12" font-weight="700" font-family="Open Sans,sans-serif" transform="rotate(-45 22 26)">NEW</text></svg>
      <div class="card-price">From GBP 3600</div>
    </div>
    <div class="card-body">
      <h3>Harrow Court , LONDON</h3>
      <p>Lorem ipsum dolor sit amet, consectetur adipisicing elit, sed do eiusmod tempor incididunt ut labore et dolore magna aliqua.</p>
      <div class="progress"><span style="width:10%"></span></div>
      <div class="stats"><span>10% Funded</span><span>8 Days Left</span></div>
      <div class="card-link">See Project Details<svg width="12" height="12" viewBox="0 0 12 12"><path d="M1 0l10 6-10 6z" fill="#add136"/></svg></div>
    </div>
  </article>

  <article class="card abs" style="left:462px">
    <div class="card-photo" role="img" aria-label="Photo of an old town square with a clock tower" style="background:linear-gradient(160deg,#e8d7b8,#b37a4f 55%,#5a3d2c)">
      <svg class="card-new" width="70" height="70" viewBox="0 0 70 70"><path d="M0 0h70L0 70z" fill="#add136"/><text x="10" y="30" fill="#fff" font-size="12" font-weight="700" font-family="Open Sans,sans-serif" transform="rotate(-45 22 26)">NEW</text></svg>
      <div class="card-price">From GBP 3600</div>
    </div>
    <div class="card-body">
      <h3>Harrow Court , LONDON</h3>
      <p>Lorem ipsum dolor sit amet, consectetur adipisicing elit, sed do eiusmod tempor incididunt ut labore et dolore magna aliqua.</p>
      <div class="progress"><span style="width:60%"></span></div>
      <div class="stats"><span>60% Funded</span><span>8 Days Left</span></div>
      <div class="card-link">See Project Details<svg width="12" height="12" viewBox="0 0 12 12"><path d="M1 0l10 6-10 6z" fill="#add136"/></svg></div>
    </div>
  </article>

  <article class="card abs" style="left:777px">
    <div class="card-photo" role="img" aria-label="Photo of a city street lined with tall buildings" style="background:linear-gradient(160deg,#d7dde2,#7f8c97 60%,#4b4f55)">
      <svg class="card-new" width="70" height="70" viewBox="0 0 70 70"><path d="M0 0h70L0 70z" fill="#add136"/><text x="10" y="30" fill="#fff" font-size="12" font-weight="700" font-family="Open Sans,sans-serif" transform="rotate(-45 22 26)">NEW</text></svg>
      <div class="card-price">From GBP 3600</div>
    </div>
    <div class="card-body">
      <h3>Harrow Court , LONDON</h3>
      <p>Lorem ipsum dolor sit amet, consectetur adipisicing elit, sed do eiusmod tempor incididunt ut labore et dolore magna aliqua.</p>
      <div class="progress"><span style="width:10%"></span></div>
      <div class="stats"><span>10% Funded</span><span>8 Days Left</span></div>
      <div class="card-link">See Project Details<svg width="12" height="12" viewBox="0 0 12 12"><path d="M1 0l10 6-10 6z" fill="#add136"/></svg></div>
    </div>
  </article>
</section>

<section class="community">
  <h2>Be Part of a Growing International Community</h2>
  <p class="lead abs">Gain access to new projects in world class cities and join our growing community of international landlords.</p>
  <div class="skyline abs" role="img" aria-label="Misty grey city skyline with a curving highway"></div>

  <div class="quote abs" style="left:160px">
    <h3>One of the Best</h3>
    <p>Lorem ipsum dolor sit amet, consectetur adipisicing elit, sed do eiusmod tempor incididunt ut labore et dolore magna aliqua.</p>
    <span class="quote-tail"></span>
  </div>
  <div class="author abs" style="left:200px"><span class="avatar" role="img" aria-label="Portrait of Daniel Brookes"></span>Daniel Brookes</div>

  <div class="quote abs" style="left:668px">
    <h3>Exellent Service</h3>
    <p>Lorem ipsum dolor sit amet, consectetur adipisicing elit, sed do eiusmod tempor incididunt ut labore et dolore magna aliqua.</p>
    <span class="quote-tail"></span>
  </div>
  <div class="author abs" style="left:708px"><span class="avatar" role="img" aria-label="Portrait of Martin Hale"></span>Martin Hale</div>
</section>

<section class="press">
  <div class="press-label abs">FEATURED IN</div>
  <div class="press-row abs">
    <span style="width:100px"></span><span style="width:110px"></span><span style="width:110px"></span><span style="width:90px"></span><span style="width:40px"></span><span style="width:110px"></span><span style="width:100px"></span>
  </div>
</section>

<footer class="site-footer">
  <div class="brand abs"><span class="brand-dot"></span>pooltenant</div>
  <p class="footer-text abs">Pooltenant is part of the Sproutline Group. The Sproutline Group is a worldwide pioneer and leader in the crowd investing, peer to peer and online investment market.</p>
  <nav class="footer-nav abs" style="left:640px"><span>Home</span><span>How it works</span><span>Discover a project</span></nav>
  <nav class="footer-nav abs" style="left:800px"><span>Blog</span><span>Find out more</span></nav>
  <div class="group-name abs">sproutline<br>group</div>
</footer>

<div class="bottom-bar abs">
  <div class="social abs">Connect with us: <i></i><i></i><i></i></div>
  <div class="legal abs">Legal statement | Privacy | © pooltenant 2014</div>
</div>

</body>
</html>
```